PLQ Biz Cards and Web Page Design

Hello we are a credit card processing company, a lending company, and payroll company. Seeing how this is a card. I would like to see some clever designs... You could make it look like a credit card, with raised lettering and signature spot on the back. Be creative.
Also this is for a webpage. Our website is www.velderpaytrust.com
Please let me know what you need.

Target Market(s)

Business Owners in the USA.

Industry/Entity Type

Credit Card

Contact Information for Business Card

I've attached our current logo and business cards. I would like you to use the Red, White, and Blue Colors and also maybe try designs that look like credit cards with Raised Text, signature spot in the back and mag strips.

Number of Pages Required

1 page

```html
<!DOCTYPE html>
<html lang="en">
<head>
<meta charset="utf-8">
<title>PLQ — Velder Pay Trust</title>
<link rel="stylesheet" href="https://fonts.googleapis.com/css2?family=Montserrat:wght@700&family=Tinos&display=swap">
<style>
  :root {
    --ink-bg: #16191a;
    --flag-red: #f0141b;
    --flag-blue: #0a22f0;
  }
  html, body {
    margin: 0;
    padding: 0;
    overflow: hidden;
    background: var(--ink-bg);
  }
  .card {
    position: relative;
    width: 1200px;
    height: 686px;
    background: var(--ink-bg);
    overflow: hidden;
  }
  .brand-square {
    position: absolute;
    left: 322px;
    top: 276px;
    width: 34px;
    height: 34px;
    background: var(--flag-blue);
  }
  .brand-initials {
    position: absolute;
    right: 654px;
    top: 248px;
    margin: 0;
    font-family: "Montserrat", sans-serif;
    font-weight: 700;
    font-size: 80px;
    line-height: 1;
    color: var(--flag-red);
  }
  .brand-divider {
    position: absolute;
    left: 576px;
    top: 177px;
    width: 3px;
    height: 231px;
    background: var(--flag-red);
  }
  .brand-name {
    margin: 0;
    font-family: "Montserrat", sans-serif;
    font-weight: 700;
    color: var(--flag-red);
  }
  .brand-name .line-main,
  .brand-name .line-sub {
    position: absolute;
    left: 618px;
    line-height: 1;
    white-space: nowrap;
  }
  .brand-name .line-main {
    top: 238px;
    font-size: 78px;
    letter-spacing: 1px;
  }
  .brand-name .line-sub {
    top: 310px;
    font-size: 24px;
    letter-spacing: 6.5px;
  }
  .site-url {
    position: absolute;
    left: 0;
    right: 0;
    top: 646px;
    margin: 0;
    text-align: center;
    font-family: "Tinos", serif;
    font-size: 32px;
    line-height: 1;
    color: var(--flag-red);
  }
</style>
</head>
<body>
  <main class="card">
    <div class="brand-square" aria-hidden="true"></div>
    <p class="brand-initials">PLQ</p>
    <div class="brand-divider" aria-hidden="true"></div>
    <h1 class="brand-name">
      <span class="line-main">VELDER</span>
      <span class="line-sub">PAY TRUST SERVICES</span>
    </h1>
    <p class="site-url">www.velderpaytrust.com</p>
  </main>
</body>
</html>
```